Mediation Website Design Upgrade

Project Details: https://files.plumvaro.net/sheet/k/8Wd3mPzqTuLhXe7nRaBo4_KcVy-92jsQ2fLgNwHd/view?ref=shared

Number of Pages Required

2 page

Font styles to use
Sans Serif

```html
<!DOCTYPE html>
<html lang="en">
<head>
<meta charset="utf-8">
<title>Harborline Mediation Group – Our Services</title>
<link rel="stylesheet" href="https://fonts.googleapis.com/css2?family=Poppins:ital,wght@0,400;0,500;0,600;1,400&display=swap">
<style>
:root{
  --teal:#5e8a84;
  --teal-dark:#4f7a74;
  --ink:#141414;
  --muted:#6f6f6f;
  --band:#f7f7f7;
  --panel:#ffffff;
  --panel-head:#eeeced;
  --line:#e6e6e6;
  --photo-a:#f1f1ef;
  --photo-b:#e4e4e0;
}
*{margin:0;padding:0;box-sizing:border-box}
html,body{width:917px;height:1200px;overflow:hidden;background:#fff}
body{font-family:'Poppins',sans-serif;color:var(--ink);position:relative}
.abs{position:absolute}

.brand{left:0;width:917px;top:34px;text-align:center;display:flex;justify-content:center;align-items:center;gap:8px}
.brand-mark{width:14px;height:14px;border-radius:50%;background:var(--teal)}
.brand-name{font-size:13px;font-weight:500;color:var(--ink);letter-spacing:-.2px}

.nav{top:107px;left:0;width:917px;display:flex;justify-content:center;gap:0}
.nav a{font-size:7.6px;font-weight:600;color:var(--ink);text-decoration:none;position:relative;margin:0 17px}
.nav a.active{color:var(--teal)}
.nav a.active::after{content:"";position:absolute;left:50%;top:16px;width:12px;height:2px;margin-left:-6px;background:var(--teal)}

.band{top:173px;left:0;width:917px;height:732px;background:var(--band)}

.side-menu{left:193px;top:187px;width:168px;height:212px;background:var(--panel)}
.side-head{height:30px;background:var(--panel-head);display:flex;align-items:center;padding-left:24px;gap:6px;font-size:7.6px;font-weight:500;color:var(--teal)}
.side-list{list-style:none;padding:10px 0 0 16px}
.side-list li{font-size:7.8px;color:var(--muted);height:25.8px;line-height:16px}

.consult{left:193px;top:421px;width:168px;height:212px;background:var(--panel);padding:0 19px}
.consult h3{font-size:7.4px;font-weight:600;margin-top:21px}
.phone{display:flex;align-items:center;gap:7px;margin-top:17px}
.phone-icon{width:26px;height:26px;border-radius:50%;background:#fff;box-shadow:0 2px 6px rgba(0,0,0,.12);display:flex;align-items:center;justify-content:center}
.phone-num{font-size:7.8px;font-weight:500;color:var(--teal)}
.consult p{font-size:6px;line-height:12px;color:var(--muted);margin-top:19px}
.btn{display:inline-block;background:var(--teal);color:#fff;font-size:6.2px;font-weight:500;text-align:center}
.consult .btn{width:61px;height:21px;line-height:21px;margin-top:19px}

.intro{left:376px;width:346px;top:0;text-align:center}
.accent{width:31px;height:4px;background:var(--teal)}
.intro-bar{left:533px;top:209px}
.title{left:376px;width:346px;top:224px;text-align:center;font-size:25px;font-weight:600;color:var(--teal)}
.lead{left:400px;width:298px;top:268px;text-align:center;font-size:8.2px;line-height:15.8px}
.intro-btn{left:510px;top:355px;width:77px;height:21px;line-height:21px}

.photo{left:376px;top:399px;width:348px;height:234px;background:linear-gradient(135deg,var(--photo-a),var(--photo-b))}

.divider-h{left:193px;top:663px;width:530px;height:1px;background:var(--line)}
.divider-v{left:503px;top:663px;width:1px;height:220px;background:var(--line)}

.focus-title{left:194px;top:694px;width:300px;font-size:7.4px;font-weight:600;line-height:14.4px}
.focus-list{left:194px;top:743px;list-style:none}
.focus-list li{display:flex;align-items:center;gap:9px;font-size:8.2px;height:19.2px}
.focus-list em{color:var(--muted)}
.chev{width:10px;height:10px;border-radius:50%;background:var(--teal);display:flex;align-items:center;justify-content:center}

.aside-bar{left:609px;top:704px;width:30px;height:1.5px;background:var(--teal)}
.aside-item{left:524px;width:200px;display:flex;gap:6px}
.aside-item p{font-size:6.2px;line-height:12.4px;color:var(--muted)}
.aside-item a{color:var(--teal);font-weight:500;font-style:italic}
.arrow-box{flex:none;width:12px;height:9px;background:var(--teal);margin-top:2px;display:flex;align-items:center;justify-content:center}

.footer{top:905px;left:0;width:917px;height:295px;background:var(--teal)}
.f-col{top:944px;color:#fff}
.f-col h4{font-size:7.8px;font-weight:600;margin-bottom:13px}
.f-col ul{list-style:none}
.f-col li{font-size:6.2px;height:14.3px;color:#eef3f2}
.connect{top:1096px;left:0;width:917px;text-align:center;color:#fff;font-size:6.2px;font-weight:500}
.socials{top:1110px;left:0;width:917px;display:flex;justify-content:center;gap:6px}
.socials span{width:7px;height:7px;background:#fff}
.copy{top:1167px;left:0;width:917px;text-align:center;color:#fff;font-size:6.2px}
</style>
</head>
<body>

<header>
  <div class="abs brand"><span class="brand-mark"></span><span class="brand-name">HARBORLINE MEDIATION GROUP</span></div>
  <nav class="abs nav">
    <a href="#">HOME</a><a href="#">CONTACT</a><a href="#">SERVICES</a><a href="#" class="active">CONFLICT CONSULTING</a><a href="#">ABOUT</a><a href="#">TOOLS</a><a href="#">BLOG</a>
  </nav>
</header>

<main>
  <div class="abs band"></div>

  <aside class="abs side-menu">
    <div class="side-head">
      <svg width="11" height="8" viewBox="0 0 11 8"><path d="M0 4h9M6 1l3 3-3 3" fill="none" stroke="#5e8a84" stroke-width="1.5"/></svg>
      SERVICES
    </div>
    <ul class="side-list">
      <li>Workplace &amp; Comercial Meditation</li>
      <li>Meeting Or Project Facilitation</li>
      <li>Conflict Coaching</li>
      <li>Negociation</li>
      <li>Family Mediation</li>
      <li>Divorce &amp; Postdivorce Meditation</li>
    </ul>
  </aside>

  <section class="abs consult">
    <h3>FREE INITIAL CONSULTATION</h3>
    <div class="phone">
      <span class="phone-icon"><svg width="11" height="11" viewBox="0 0 24 24"><path d="M6.6 10.8a15 15 0 0 0 6.6 6.6l2.2-2.2a1 1 0 0 1 1-.25 11.4 11.4 0 0 0 3.6.6 1 1 0 0 1 1 1V20a1 1 0 0 1-1 1A17 17 0 0 1 3 4a1 1 0 0 1 1-1h3.5a1 1 0 0 1 1 1c0 1.25.2 2.45.6 3.6a1 1 0 0 1-.25 1z" fill="#5e8a84"/></svg></span>
      <span class="phone-num">555-014-2290</span>
    </div>
    <p>Click The Button Below To Detail The Best Way To Contact You Here And Marta Will Call Or Email You To Arrange A No Cost Informational Session.</p>
    <a class="btn">Fill Out Form</a>
  </section>

  <div class="abs accent intro-bar"></div>
  <h1 class="abs title">Our Services</h1>
  <p class="abs lead">Providing effective, high quality conflict consulting is the mission of harborline mediation group. a key way we work towards meeting this mission is to specialize in selected services that distinguish our firm in the growing conflict consulting field.</p>
  <a class="abs btn intro-btn">Free Consultation</a>

  <div class="abs photo" role="img" aria-label="Photo of two hands fitting wooden puzzle pieces together on a light background"></div>

  <div class="abs divider-h"></div>
  <div class="abs divider-v"></div>

  <h2 class="abs focus-title">BASED UPON EXPERIENCE, EDUCATION, AND PASSION, FIVE FOCUS AREAS HAVE BEEN IDENTIFIED:</h2>
  <ul class="abs focus-list">
    <li><span class="chev"><svg width="5" height="6" viewBox="0 0 5 6"><path d="M1 1l2 2-2 2" fill="none" stroke="#fff" stroke-width="1.2"/></svg></span>Conflict Coaching</li>
    <li><span class="chev"><svg width="5" height="6" viewBox="0 0 5 6"><path d="M1 1l2 2-2 2" fill="none" stroke="#fff" stroke-width="1.2"/></svg></span>Adult Sibling And /Or Elder Mediation</li>
    <li><span class="chev"><svg width="5" height="6" viewBox="0 0 5 6"><path d="M1 1l2 2-2 2" fill="none" stroke="#fff" stroke-width="1.2"/></svg></span><span>Commercial Mediation (<em>Both Between And Within Business Enterprises</em>)</span></li>
    <li><span class="chev"><svg width="5" height="6" viewBox="0 0 5 6"><path d="M1 1l2 2-2 2" fill="none" stroke="#fff" stroke-width="1.2"/></svg></span><span>Facilitation – <em>Project Or Meeting</em></span></li>
    <li><span class="chev"><svg width="5" height="6" viewBox="0 0 5 6"><path d="M1 1l2 2-2 2" fill="none" stroke="#fff" stroke-width="1.2"/></svg></span>Negotiation</li>
  </ul>

  <div class="abs aside-bar"></div>
  <div class="abs aside-item" style="top:725px">
    <span class="arrow-box"><svg width="7" height="5" viewBox="0 0 7 5"><path d="M0 2.5h6M4 .5l2 2-2 2" fill="none" stroke="#fff" stroke-width="1"/></svg></span>
    <p>Whether For Your Business, Nonprofit Organization Or Family And Personal Issues, You Can Explore Mutually Satisfying Solutions Through Our Caring And Professional Mediation Practice.</p>
  </div>
  <div class="abs aside-item" style="top:801px">
    <span class="arrow-box"><svg width="7" height="5" viewBox="0 0 7 5"><path d="M0 2.5h6M4 .5l2 2-2 2" fill="none" stroke="#fff" stroke-width="1"/></svg></span>
    <p>One More Thing! If You Are Not Sure Your Need Fits Into Our Specialties, <a>Contact Us</a> And We Will Explore Options With You.</p>
  </div>
</main>

<footer>
  <div class="abs footer"></div>
  <div class="abs f-col" style="left:208px"><h4>Home</h4><ul><li>About Us</li><li>Our Services</li><li>BLOG</li><li>Contact Us</li></ul></div>
  <div class="abs f-col" style="left:303px"><h4>What Makes Us Different</h4><ul><li>Our Philosophy</li><li>Dana's Biography</li><li>Marta's Biography</li><li>Our Associates</li></ul></div>
  <div class="abs f-col" style="left:452px"><h4>Learn About Mediation Services</h4><ul><li>Commercial Mediation</li><li>Conflict Coaching</li><li>Elder &amp; Adult Sibling Mediation</li><li>Meeting Or Project Facilitation</li><li>Negotiation</li><li>Divorce &amp; Post-Divorce Mediation</li></ul></div>
  <div class="abs f-col" style="left:629px"><h4>Conflict Consulting</h4><ul><li>Who Should Work With Us</li><li>Values &amp; Benefits</li><li>Outcomes</li></ul></div>
  <div class="abs connect">Conect With Us</div>
  <div class="abs socials"><span></span><span></span><span></span></div>
  <div class="abs copy">Copyright © 2014 HMG. All Rights Reserved.</div>
</footer>

</body>
</html>
```